Business Card Makeover. Recreate a sleek modern design for our business card.

DO NOT COPY OUR CURRENT DESIGN. MUST BE ONE SIDED BUSINESS CARD.
Create a new business card design, using our new logo. Attached is a sample of our current design and new logo. Please note the address and email will change. The new address is 417 Corvell West Palm Beach 33472 and our website will be www.talvendrake.example.

We are an architectural and interior design firm. We prefer a clean modern look. Something that is refined and emulates excellence.

Industry/Entity Type

Architecture

Contact Information for Business Card

clean modern look, please do not copy our attached design.

Font styles to use
Other font styles liked:
• see attached business card font

Colors

Designer to choose colors to be used in the design.

Requirements
Must have
• Must have a modern appeal and resemble our current branding.
Nice to have
• modern font, our logo, legible name and titles progressive design
Should not have
• Do not add colors not reflected in our branding. Should not look like our current card.

```html
<!DOCTYPE html>
<html lang="en">
<head>
<meta charset="utf-8">
<title>Talven Drake + Partners — Business Cards</title>
<link href="https://fonts.googleapis.com/css2?family=Open+Sans:wght@400;700;800&family=Cabin:wght@400&display=swap" rel="stylesheet">
<style>
  :root {
    --brand-blue: #1a7fc9;
    --card-white: #ffffff;
    --backdrop: #e9eaec;
    --card-shadow: rgba(0,0,0,0.18);
  }
  * { margin: 0; padding: 0; box-sizing: border-box; }
  html, body { width: 1200px; height: 899px; overflow: hidden; }
  body { background: var(--backdrop); position: relative; }

  .card {
    position: absolute;
    width: 640px;
    height: 366px;
    background: var(--card-white);
    box-shadow: 0 8px 24px var(--card-shadow);
    color: var(--brand-blue);
    overflow: hidden;
  }
  .card--director { left: 120px; top: 60px; }
  .card--architect { left: 440px; top: 473px; }

  .firm-mark {
    position: absolute; left: 40px; top: 92px;
    display: flex; align-items: center; gap: 12px;
  }
  .firm-mark__dot {
    width: 44px; height: 44px; border-radius: 50%;
    background: var(--brand-blue); flex: none;
  }
  .firm-mark__name {
    font-family: "Open Sans", sans-serif; font-weight: 400;
    font-size: 19px; letter-spacing: 1px; line-height: 22px;
    color: var(--brand-blue); width: 170px;
  }

  .dash {
    display: block; width: 60px; height: 2px;
    background: repeating-linear-gradient(90deg, var(--brand-blue) 0 12px, transparent 12px 18px);
  }

  .contact {
    position: absolute; left: 52px; top: 158px;
    font-family: "Cabin", sans-serif; font-size: 14.5px; line-height: 18px;
  }
  .contact .dash { margin: 7px 0; }
  .contact__phones { padding-left: 6px; }
  .contact__address { padding-left: 14px; }

  .person {
    position: absolute; right: 40px; top: 36px; width: 300px; text-align: right;
    font-family: "Open Sans", sans-serif;
  }
  .person__name { font-weight: 800; font-size: 27px; letter-spacing: 1.5px; line-height: 32px; }
  .person__title { font-weight: 400; font-size: 15px; letter-spacing: 1.2px; line-height: 20px; }
  .person__credentials { font-weight: 800; font-size: 20px; letter-spacing: 1px; line-height: 26px; }
  .person__credentials sup { font-size: 11px; }

  .practice {
    position: absolute; right: 40px; top: 170px; width: 280px;
    text-align: center; font-family: "Open Sans", sans-serif;
    font-weight: 800; font-size: 27px; letter-spacing: 1.5px; line-height: 30px;
  }
  .practice--lower { top: 185px; }
  .practice .dash { margin: 10px auto; }
  .practice__plus { display: block; font-size: 26px; line-height: 24px; }
</style>
</head>
<body>

  <article class="card card--director">
    <div class="person">
      <div class="person__name">Marcus Whitford</div>
      <div class="person__title">Partner, Director of Design</div>
    </div>
    <div class="firm-mark">
      <span class="firm-mark__dot"></span>
      <span class="firm-mark__name">TALVEN DRAKE + PARTNERS</span>
    </div>
    <div class="contact">
      <span class="dash"></span>
      <div class="contact__phones">
        C: 561.555.0142<br>
        O: 561.555.0180<br>
        F: 561.555.0193
      </div>
      <span class="dash"></span>
      <div class="contact__address">
        417 Corvell Street<br>
        West Palm Beach, FL 33472<br>
        marcus@talvendrake.example<br>
        www.talvendrake.example<br>
        LIC.# AA48117203
      </div>
    </div>
    <div class="practice">
      <span class="dash"></span>
      Architecture
      <span class="practice__plus">+</span>
      Interior Design
      <span class="dash"></span>
    </div>
  </article>

  <article class="card card--architect">
    <div class="person">
      <div class="person__name">Elena Sorvik</div>
      <div class="person__title">Partner, Project Architect</div>
      <div class="person__credentials">AIA, LEED<sup>®</sup> AP</div>
    </div>
    <div class="firm-mark">
      <span class="firm-mark__dot"></span>
      <span class="firm-mark__name">TALVEN DRAKE + PARTNERS</span>
    </div>
    <div class="contact">
      <span class="dash"></span>
      <div class="contact__phones">
        O: 561.555.0180<br>
        F: 561.555.0193
      </div>
      <span class="dash"></span>
      <div class="contact__address">
        417 Corvell Street<br>
        West Palm Beach, FL 33472<br>
        elena@talvendrake.example<br>
        www.talvendrake.example<br>
        LIC.# AA48117203
      </div>
    </div>
    <div class="practice practice--lower">
      <span class="dash"></span>
      Architecture
      <span class="practice__plus">+</span>
      Interior Design
      <span class="dash"></span>
    </div>
  </article>

</body>
</html>
```